copper lantern website

We need a new website for our new business division. We are a sustainable design firm specializing in servicing the needs if architects and developers. We have a staff consisting of architects, engineers, and former contractors and we understand green must make sense.

Bottomline - the only sustainable and copper lantern solutions are those thatbare good for the environment and good for our clients bottom line.

Our company is copper lantern and we will send you a copy of our logo you will see our tagline. Is simple. sustainable. solutions. The play with the periods is that we believe their are simple sustainable solutions and we want to use the words together and possible let each stand alone to accentuate their individual meaning in regards to benefit to our clients.

We want a cool splash page with nich graphics and pictures then later pages to feature projects and design ideas.

Target Market(s)

Our target customers are architects, developers, and contractors who would need assistance with the design process for a VARN project or assisatnce with a building owner who wants to make tehir facilty more environmentally friendly and save energy costs at the same tiem.

Industry/Entity Type

Environment

Requirements
Must have
• Needs a construction look with an environmentally friendly surrounding that is pleasing to look at. Must appeal to the client not only as environmentally friendly but also a wise investment.
Nice to have
• Opportunity for a connection to Social networking including a blog.
Should not have
• A totally environmental building feel at whatever cost. We want to emphasize that it is possible to build environmental friendly and save you money over the life of your building

```html
<!DOCTYPE html>
<html lang="en">
<head>
<meta charset="utf-8">
<title>copper lantern — sustainable design</title>
<link rel="stylesheet" href="https://fonts.googleapis.com/css2?family=Alegreya+Sans+SC:wght@400;500&display=swap">
<style>
:root{
  --page-bg:#cfcfcf;
  --panel:#e6e6e6;
  --dark:#2a0d07;
  --green:#3f9a36;
  --green-dark:#2c7a26;
  --nav-gray:#6a6a6a;
  --tab-gray:#777777;
  --text:#1c1c1c;
  --white:#ffffff;
}
*{box-sizing:border-box;margin:0;padding:0}
html,body{width:1200px;height:795px;overflow:hidden;background:var(--page-bg)}
body{font-family:"Alegreya Sans SC",sans-serif;color:var(--text);position:relative}
.site{position:absolute;left:122px;top:47px;width:957px;height:698px}
.abs{position:absolute}
.topbar{left:0;top:0;width:957px;height:17px;background:var(--dark);border-bottom:3px solid var(--green)}
.shine{left:0;top:20px;width:957px;height:27px;background:linear-gradient(90deg,#9a9a9a 0%,#eeeeee 45%,#f4f4f4 60%,#8a8a8a 100%)}
.hero{left:0;top:47px;width:957px;height:210px;background:var(--panel)}
.hero-art{left:0;top:20px;width:452px;height:237px;background:linear-gradient(100deg,#4fb046 0%,#86cf7e 35%,#cfe8cb 75%,var(--panel) 100%)}
.brand{left:156px;top:178px;width:218px;height:60px;background:var(--white);display:flex;align-items:center;gap:8px;padding-left:14px}
.brand-dot{width:16px;height:16px;border-radius:50%;background:var(--green-dark)}
.brand-name{font-size:24px;font-weight:500;color:var(--green-dark)}
.hero-copy{left:473px;top:65px;width:484px;font-size:14px;letter-spacing:.45px;line-height:16.4px;white-space:nowrap}
.hero-copy p+p{margin-top:16px}
.nav{left:0;top:257px;width:957px;height:26px;background:var(--nav-gray);border-bottom:1px solid #9a9a9a}
.nav ul{list-style:none;display:flex;gap:2px;position:absolute;left:122px;top:0}
.nav li{width:139.5px;height:26px;background:var(--white);font-size:15px;letter-spacing:.3px;text-align:center;line-height:26px}
.tab{height:22px;color:var(--white);font-size:14px;letter-spacing:.3px;line-height:22px;padding-left:14px;background:var(--tab-gray);clip-path:polygon(0 0,82% 0,100% 100%,0 100%)}
.card{background:var(--panel);font-size:13px;letter-spacing:.35px;line-height:16.5px;padding:12px 10px;white-space:nowrap;overflow:hidden;clip-path:polygon(0 0,calc(100% - 24px) 0,100% 14px,100% 100%,0 100%)}
.band{left:0;top:451px;width:957px;height:213px;background:var(--dark)}
.gtab{height:21px;background:var(--green);color:var(--white);font-size:15px;letter-spacing:.3px;line-height:21px;padding-left:18px;clip-path:polygon(0 0,78% 0,100% 100%,0 100%)}
.box{background:var(--panel);border:2px solid var(--green);font-size:13px;letter-spacing:.35px;line-height:16.4px;white-space:nowrap;overflow:hidden}
.box p+p{margin-top:16px}
.news-side{background:var(--white);font-size:13px;letter-spacing:.35px;line-height:16.4px;padding:10px 16px;white-space:nowrap;overflow:hidden}
.follow{color:var(--green);font-size:14px}
.socials{display:flex;gap:8px;margin-top:6px}
.socials span{font-size:11px;color:#555}
.footer{left:0;top:664px;width:957px;height:34px;background:linear-gradient(90deg,#6b3a1f 0%,#3a190d 20%,#5a2c16 45%,#2a0d07 75%,#4a2210 100%);color:var(--white);font-size:14px;line-height:34px}
.footer .copy{position:absolute;left:18px;color:#1a0804}
.footer .links{position:absolute;right:18px;display:flex;gap:10px}
</style>
</head>
<body>
<div class="site">
  <div class="abs topbar"></div>
  <div class="abs shine"></div>
  <div class="abs hero"></div>
  <div class="abs hero-art" role="img" aria-label="Green illustration of glass towers, a world map and a young plant sprouting"></div>
  <div class="abs brand"><span class="brand-dot"></span><span class="brand-name">copper lantern</span></div>
  <div class="abs hero-copy">
    <p>In sit amet pede quis leo vulputate hendrerit. Cras lao reet leo et<br>justo auctor condimentum. Integer id enim.<br>Suspendisse egestas, dui ac egestas mollis, libero orci hendrerit lacus<br>et malesuada lorem neque ac libero. Morbi tempor pulvinar pede. Donec<br>vel elit.</p>
    <p>Sed placerat accumsan ligula. Aliquam felis magna, congue quis, tempus<br>eu, aliquam vitae, ante. Cras neque justo, ultrices at, rhoncus a, facilisis<br>eget, nisl. Quisque vitae pede. Nam et augue. Sed a elit. Ut vel massa.<br>Suspendisse nibh pede, ultrices vitae, ultrices nec, mollis non, nibh.</p>
  </div>
  <nav class="abs nav"><ul><li>Products</li><li>Education</li><li>Clients</li><li>Company</li><li>Support</li></ul></nav>

  <div class="abs tab" style="left:0;top:292px;width:198px">Let us help</div>
  <div class="abs card" style="left:0;top:313px;width:300px;height:137px">Quisque vitae pede. Nam et augue. Sed a elit.<br>Ut vel massa. Suspendisse nibh pede, ultrices<br>vitae, ultrices nec, mollis non, nibh. In sit amet<br>pede quis leo vulputate hendrerit.<br>Suspendisse nibh pede, ultrices vitae.</div>

  <div class="abs tab" style="left:307px;top:314px;width:200px">Client</div>
  <div class="abs card" style="left:307px;top:336px;width:335px;height:114px">Suspendisse egestas, dui ac egestas mollis, libero<br>orci hendrerit lacus, et malesuada lorem neque ac<br>libero. Morbi tempor pulvinar pede.<br>Donec vel elit.</div>

  <div class="abs tab" style="left:649px;top:342px;width:166px">What we are</div>
  <div class="abs card" style="left:649px;top:364px;width:308px;height:86px">Cras neque justo, ultrices at, rhoncus a,<br>facilisis eget, nisl. Quisque vitae pede. Nam et<br>augue. Sed a elit. Ut vel massa. Suspendisse nibh<br>pede, ultrices vitae, ultrices nec.</div>

  <div class="abs band"></div>
  <div class="abs gtab" style="left:0;top:457px;width:198px">Services</div>
  <div class="abs box" style="left:0;top:478px;width:473px;height:186px;padding:12px 16px">
    <p>Quisque vitae<br>Quisque vitae pede. Nam et augue. Sed a elit. Ut vel massa.<br>Suspendisse nibh pede, ultrices vitae, ultrices nec, mollis non, nibh.<br>Quisque vitae pede. Nam et augue. Sed a elit. Ut vel massa.</p>
    <p>Suspendisse<br>nibh pede, ultrices vitae, ultrices nec, mollis non, nibh.<br>Quisque vitae pede. Nam et augue. Sed a elit. Ut vel massa.<br>Suspendisse nibh pede, ultrices vitae, ultrices nec, mollis non, nibh.</p>
  </div>

  <div class="abs gtab" style="left:483px;top:457px;width:198px">News</div>
  <div class="abs box" style="left:483px;top:478px;width:474px;height:186px;padding:14px 18px">
    <p><span style="font-size:14.5px">May 3, 2011...</span><br>Quisque vitae pede. Nam et augue.<br>Sed a elit.<br>Quisque vitae pede. Nam et augue.<br>Sed a elit. Ut vel massa.</p>
    <p><span style="font-size:14.5px">May 3, 2011...</span><br>Quisque vitae pede. Nam et augue.<br>Sed a elit. Ut vel massa..</p>
  </div>
  <div class="abs news-side" style="left:730px;top:486px;width:218px;height:103px;padding-top:12px">Cras neque justo, ultrices at,<br>rhoncus a, facilisis eget, nisl.<br>Quisque vitae pede.<br>Sed a elit. Ut vel massa. Suspen<br>disse nibh pede, ultrices vitae.</div>
  <div class="abs news-side" style="left:730px;top:594px;width:218px;height:61px">
    <div class="follow">Follow us</div>
    <div class="socials"><span>Chirper</span><span>Friendlink</span><span>Feed</span><span>Reelhub</span></div>
  </div>

  <footer class="abs footer"><span class="copy">Copyright 2011</span><span class="links"><span>Privacy policy</span><span>Site map</span></span></footer>
</div>
</body>
</html>
```